lifestyle photographer promotion piece

I would like to create a printed postcard to send to potential clients to introduce them to my work and hopefully create new clients. I'm a commercial photographer who just relocated to the Miami area and would really like to be getting more luxury lifestyle and resort work that includes my unique ability to shoot every aspect of lifestyle including food, travel, lifestyle and fashion. I'd like to incorporate between 4-12 of my best images from my online portfolio at www.lunadekkerfoto.com. The printed piece should also have a very clean, graphic, modern feel to it overall similar to my website. The main goal is to create a striking and compelling grouping of images showing my diverse offerings but in a way that shows an obvious visual style, my style. Please refer to my website for images. When winner is chosen, I will supply hi-res files to compete the design.
Updates

The card is a mailer and a handout. The back of the card should be black and white and text only with my info and an area for address to information. Dimensions of the card are 6x8.5 inches and I prefer the horizontal aspect ratio.

I've noticed a few designers are incorporating graphics. I would like to avoid that. Interested in photography dominated card with /or without graphic use of white space. I tend to avoid color backgrounds, white space is my preference in most cases although I'm not completely against it. 

Target Market(s)

Advertising Agencies and Magazines, Record Labels, Modeling Agencies, Public Relations Firms

Industry/Entity Type

Fashion

Requirements
Must have
• Horizontal

Front(color):
Marisol Tate Photography
Miami / Naples / New York

Back(black and white):
(239)614-2938
www.lunadekkerfoto.com
info@lunadekkerfoto.com

```html
<!DOCTYPE html>
<html lang="en">
<head>
<meta charset="utf-8">
<title>Marisol Tate Photography – Postcard</title>
<link rel="stylesheet" href="https://fonts.googleapis.com/css2?family=Noto+Serif:wght@400;700&family=PT+Sans&display=swap">
<style>
  :root {
    --page: #ffffff;
    --panel: #2b2828;
    --ink: #ffffff;
    --ornament: #4a4646;
    --corner: #a3a3a3;
  }
  * { box-sizing: border-box; margin: 0; padding: 0; }
  html, body { width: 1200px; height: 900px; overflow: hidden; background: var(--page); }
  .card {
    position: absolute; left: 16px; top: 40px; width: 1164px; height: 828px;
    background: var(--panel); overflow: hidden;
  }
  .ornament { position: absolute; border-radius: 40%; opacity: .55; }
  .ornament--tl { left: 30px; top: 30px; width: 230px; height: 230px; background: radial-gradient(circle, var(--ornament), transparent 70%); }
  .ornament--tr { right: 30px; top: 30px; width: 230px; height: 260px; background: radial-gradient(circle, var(--ornament), transparent 70%); }
  .ornament--bl { left: 30px; bottom: 60px; width: 300px; height: 260px; background: radial-gradient(circle, var(--ornament), transparent 70%); }
  .ornament--br { right: 30px; bottom: 20px; width: 260px; height: 260px; background: radial-gradient(circle, var(--ornament), transparent 70%); }
  .ornament--mid { left: 600px; top: 300px; width: 300px; height: 360px; background: radial-gradient(circle, var(--ornament), transparent 70%); }

  .brand {
    position: absolute; left: 74px; top: 106px;
    font-family: "Noto Serif", serif; font-weight: 700; font-size: 43px;
    color: var(--ink); letter-spacing: .5px; text-shadow: 2px 2px 3px #000;
  }
  .tagline {
    position: absolute; left: 54px; top: 168px;
    font-family: "Noto Serif", serif; font-size: 16.5px; color: var(--ink); letter-spacing: .3px;
  }
  .photo { position: absolute; }
  .photo--canoe { left: 88px; top: 239px; width: 359px; height: 238px; background: linear-gradient(160deg, #4f6232, #8c8a5a 45%, #d9d4c4 70%, #a9a08a); }
  .photo--pier { left: 568px; top: 67px; width: 336px; height: 224px; background: linear-gradient(180deg, #5e89bd, #c9d6e2 40%, #7da0c4 55%, #b49c78 80%, #3f5e82); }
  .photo--flower { left: 420px; top: 463px; width: 182px; height: 274px; background: radial-gradient(circle at 45% 40%, #9a9a9a, #3c3c3c 60%, #1e1e1e); }
  .photo--food { left: 885px; top: 262px; width: 208px; height: 312px; background: radial-gradient(circle at 55% 45%, #c5793a, #9c8a6e 45%, #7b7670 80%); }
  .corner { position: absolute; width: 46px; height: 46px; background: var(--corner); }
  .corner--flower { left: 408px; top: 451px; }
  .corner--food { left: 873px; top: 251px; }

  .services { list-style: none; font-family: "Noto Serif", serif; font-weight: 700; font-size: 25px; color: var(--ink); }
  .services li { position: absolute; white-space: nowrap; }

  .contact {
    position: absolute; top: 744px; left: 0; width: 100%; height: 30px;
    font-family: "PT Sans", sans-serif; font-size: 18.5px; color: var(--ink);
  }
  .contact span, .contact svg { position: absolute; }
  .contact svg { fill: none; stroke: var(--ink); stroke-width: 1.8; }
</style>
</head>
<body>
<main class="card">
  <div class="ornament ornament--tl" role="img" aria-label="faint leafy vine ornament"></div>
  <div class="ornament ornament--tr" role="img" aria-label="faint leafy vine ornament"></div>
  <div class="ornament ornament--bl" role="img" aria-label="faint leafy vine ornament"></div>
  <div class="ornament ornament--br" role="img" aria-label="faint leafy vine ornament"></div>
  <div class="ornament ornament--mid" role="img" aria-label="faint leafy vine ornament"></div>

  <h1 class="brand">MARISOL TATE</h1>
  <p class="tagline">PHOTOGRAPHER /DIRECTIONS OF PHOTOGRAPHY</p>

  <div class="photo photo--canoe" role="img" aria-label="Lifestyle photo: woman with a dog paddling a canoe on a river"></div>
  <div class="photo photo--pier" role="img" aria-label="Travel photo: wooden pier stretching into calm water under clouds"></div>
  <div class="corner corner--food"></div>
  <div class="photo photo--food" role="img" aria-label="Food photo: fried shrimp skewers in a wire basket with dipping sauce"></div>
  <div class="corner corner--flower"></div>
  <div class="photo photo--flower" role="img" aria-label="Black and white photo of a blooming flower"></div>

  <ul class="services">
    <li style="left:616px;top:342px">.STYLE LIFE</li>
    <li style="left:697px;top:406px">.FASHION</li>
    <li style="left:616px;top:470px">.TRAVELS</li>
    <li style="left:705px;top:534px">.COVERS</li>
    <li style="left:624px;top:598px">.FOOD</li>
    <li style="left:715px;top:662px">.PORTRAIT</li>
  </ul>

  <div class="contact">
    <span style="left:64px;top:2px">NAPOLES / MIAMI / NEW YORK</span>
    <svg style="left:368px;top:-2px" width="28" height="28" viewBox="0 0 24 24"><path style="fill:var(--ink);stroke:none" d="M6.6 10.8a15 15 0 0 0 6.6 6.6l2.2-2.2c.3-.3.7-.4 1-.2 1.1.4 2.3.6 3.6.6.6 0 1 .4 1 1V20c0 .6-.4 1-1 1A17 17 0 0 1 3 4c0-.6.4-1 1-1h3.5c.6 0 1 .4 1 1 0 1.3.2 2.5.6 3.6.1.3 0 .7-.2 1z"/></svg>
    <span style="left:404px;top:2px">239.614.2938</span>
    <svg style="left:540px;top:2px" width="28" height="20" viewBox="0 0 28 20"><rect x="1" y="1" width="26" height="18" style="fill:var(--ink);stroke:none"/><path d="M1 1l13 10L27 1" style="stroke:var(--panel)"/></svg>
    <span style="left:578px;top:0">INFO@LUNADEKKERFOTO.COM</span>
    <svg style="left:838px;top:-1px" width="26" height="26" viewBox="0 0 26 26"><circle cx="13" cy="13" r="11.5"/><ellipse cx="13" cy="13" rx="5" ry="11.5"/><path d="M1.5 13h23M3.5 7h19M3.5 19h19M13 1.5v23"/></svg>
    <span style="left:876px;top:0">WWW.LUNADEKKERFOTO.COM</span>
  </div>
</main>
</body>
</html>
```